Vemtra Group: Business Card for a high end technology company

We need a cool new design for our business cards using our cloud logo. We are a technology consulting business. We pride ourselves on be the best of the best. We mainly focus on cloud solutions and managed services. We need a business card that sets us apart from the other technology companies in the area and allows us to stand out.

Target Market(s)

Technology departments, CIO, CEOs, and Information Technology Staff.

Industry/Entity Type

Information Technology

Contact Information for Business Card

Must have the logo and our name.
Must have employee name, email address, office phone, cell phone and website.
Need to have all info on one side a cool design on backside.

Font styles to use
Serif
Sans Serif

Requirements
Must have
• Must have the logo and our name.
• Must have employee name, email address, office phone, cell phone and website.
• Need to have all info on one side a cool design on back side.
• Must be a crisp clean design, not too busy or confusing.

```html
<!DOCTYPE html>
<html lang="en">
<head>
<meta charset="utf-8">
<title>Vemtra Group — Business Cards</title>
<link href="https://fonts.googleapis.com/css2?family=Quicksand:wght@400;500&family=Open+Sans:wght@400;700&display=swap" rel="stylesheet">
<style>
  :root {
    --page: #ecebe8;
    --blue-light: #8fdcec;
    --blue-mid: #2cb4e3;
    --blue-deep: #0a77c4;
    --accent: #3aa7e6;
    --ink: #3d3d3f;
    --ink-soft: #5a5a5c;
    --rule: #4a4a4a;
    --card-white: #f7f7f7;
  }
  * { margin: 0; padding: 0; box-sizing: border-box; }
  html, body {
    width: 1200px; height: 902px; overflow: hidden;
    background: var(--page);
  }
  .canvas { position: relative; width: 1200px; height: 902px; }

  .card {
    position: absolute;
    width: 560px; height: 320px;
    border-radius: 3px;
    box-shadow: 0 6px 18px rgba(0,0,0,0.18);
    overflow: hidden;
  }

  /* Front: brand side */
  .card-front {
    left: 70px; top: 80px;
    background: linear-gradient(150deg, var(--blue-light) 0%, var(--blue-mid) 50%, var(--blue-deep) 100%);
    color: #fff;
    display: flex; flex-direction: column; align-items: center; justify-content: center;
  }
  .front-brand {
    display: flex; align-items: center; gap: 16px;
    font-family: "Quicksand", sans-serif; font-weight: 400;
    font-size: 56px; letter-spacing: 0.5px; color: #fff;
  }
  .front-brand .dot {
    width: 34px; height: 34px; border-radius: 50%; background: #fff;
  }
  .front-url {
    margin-top: 14px;
    font-family: "Open Sans", sans-serif; font-weight: 700;
    font-size: 17px; color: #fff; letter-spacing: 0.3px;
  }

  /* Back: info side */
  .card-info {
    left: 570px; top: 500px;
    background: linear-gradient(160deg, #fff 0%, var(--card-white) 60%, #e9e9e9 100%);
    color: var(--ink);
  }
  .info-brand {
    position: absolute; left: 36px; top: 48px;
    display: flex; align-items: center; gap: 12px;
    font-family: "Quicksand", sans-serif; font-weight: 400;
    font-size: 40px; color: var(--ink-soft);
  }
  .info-brand .dot {
    width: 26px; height: 26px; border-radius: 50%; background: var(--accent);
  }
  .info-url {
    position: absolute; left: 74px; top: 104px;
    font-family: "Open Sans", sans-serif; font-size: 12px; color: var(--ink-soft);
  }
  .rule-name {
    position: absolute; left: 250px; right: 0; top: 150px;
    height: 1px; background: var(--rule);
  }
  .employee-name {
    position: absolute; right: 30px; top: 116px;
    background: linear-gradient(160deg, #fafafa, #f1f1f1);
    padding: 0 10px;
    font-family: "Open Sans", sans-serif; font-weight: 700;
    font-size: 24px; color: var(--ink);
  }
  .rule-contact {
    position: absolute; left: 36px; right: 200px; top: 178px;
    height: 1px; background: var(--rule);
  }
  .contact-list {
    position: absolute; left: 36px; top: 192px;
    list-style: none;
    font-family: "Open Sans", sans-serif; font-size: 13.5px; color: var(--ink);
  }
  .contact-list li {
    display: flex; align-items: center; gap: 12px;
    height: 23px;
  }
  .contact-list .icon {
    width: 14px; height: 14px; background: var(--accent);
    border-radius: 2px; flex: none;
  }
</style>
</head>
<body>
<div class="canvas">

  <section class="card card-front" aria-label="Card front">
    <div class="front-brand"><span class="dot"></span><span>Vemtra Group</span></div>
    <div class="front-url">www.vemtragroup.com</div>
  </section>

  <section class="card card-info" aria-label="Card back with contact details">
    <div class="info-brand"><span class="dot"></span><span>Vemtra Group</span></div>
    <div class="info-url">www.vemtragroup.com</div>

    <div class="rule-name"></div>
    <div class="employee-name">Corin Vale</div>

    <div class="rule-contact"></div>
    <ul class="contact-list">
      <li>
        <svg class="icon" viewBox="0 0 14 14" aria-hidden="true"><rect width="14" height="14" rx="2" fill="#3aa7e6"/><path d="M4 3.5h2l.6 2-1 .8a5 5 0 0 0 2.1 2.1l.8-1 2 .6v2c0 .5-.4.8-.9.8A7 7 0 0 1 3.2 4.4c0-.5.3-.9.8-.9z" fill="#fff"/></svg>
        <span>470.555.0142</span>
      </li>
      <li>
        <svg class="icon" viewBox="0 0 14 14" aria-hidden="true"><rect width="14" height="14" rx="2" fill="#3aa7e6"/><rect x="4.5" y="2.5" width="5" height="9" rx="1" fill="#fff"/><rect x="5.3" y="3.6" width="3.4" height="5.6" fill="#3aa7e6"/></svg>
        <span>458.555.0198</span>
      </li>
      <li>
        <svg class="icon" viewBox="0 0 14 14" aria-hidden="true"><rect width="14" height="14" rx="2" fill="#3aa7e6"/><rect x="3" y="4" width="8" height="6" fill="#fff"/><path d="M3 4l4 3.2L11 4" fill="none" stroke="#3aa7e6" stroke-width="0.9"/></svg>
        <span>info@vemtragroup.com</span>
      </li>
      <li>
        <svg class="icon" viewBox="0 0 14 14" aria-hidden="true"><rect width="14" height="14" rx="2" fill="#3aa7e6"/><circle cx="7" cy="7" r="3.8" fill="none" stroke="#fff" stroke-width="1"/><path d="M3.2 7h7.6M7 3.2c-1.6 2.2-1.6 5.4 0 7.6M7 3.2c1.6 2.2 1.6 5.4 0 7.6" fill="none" stroke="#fff" stroke-width="0.8"/></svg>
        <span>www.vemtragroup.com</span>
      </li>
      <li>
        <svg class="icon" viewBox="0 0 14 14" aria-hidden="true"><rect width="14" height="14" rx="2" fill="#3aa7e6"/><path d="M7 11.5S3.8 8 3.8 5.8a3.2 3.2 0 0 1 6.4 0C10.2 8 7 11.5 7 11.5z" fill="#fff"/><circle cx="7" cy="5.8" r="1.1" fill="#3aa7e6"/></svg>
        <span>2400 Larkspur Ave Suite 310, Harlow, GA 30512</span>
      </li>
    </ul>
  </section>

</div>
</body>
</html>
```